Copperleaf Grill
there is none
Copperleaf Grill -
Simple
Danielle Whitcomb
Proprietor
318 Ferrand Street New Orleans, LA 70119
dwhitcomb@copperleaf-eats.com
www.copperleaf-eats.com
Use the same font of Grill and New Orleans for information on card
Just put the logo and website on the back of the card

```html
<!DOCTYPE html>
<html lang="en">
<head>
<meta charset="utf-8">
<title>Copperleaf Grill Stationery</title>
<link href="https://fonts.googleapis.com/css2?family=Lato:wght@400;700&display=swap" rel="stylesheet">
<style>
  :root {
    --stage: #e9e9e9;
    --paper: #ffffff;
    --wine: #7a2230;
    --ink: #262626;
    --muted: #555555;
    --shadow: 0 2px 6px rgba(0,0,0,.18);
  }
  * { box-sizing: border-box; margin: 0; padding: 0; }
  html, body { width: 1200px; height: 866px; overflow: hidden; }
  body { background: var(--stage); font-family: 'Lato', sans-serif; color: var(--ink); position: relative; }
  .sheet { position: absolute; background: var(--paper); box-shadow: var(--shadow); overflow: hidden; }
  .wave { position: absolute; left: 0; bottom: 0; width: 100%; }

  .brand { position: absolute; text-align: center; white-space: nowrap; }
  .wordmark { font-weight: 700; color: var(--ink); letter-spacing: .3px; line-height: 1.1; }
  .tagline { color: var(--wine); font-weight: 400; letter-spacing: 3px; text-transform: uppercase; margin-top: 3px; }
  .brand.light .wordmark, .brand.light .tagline { color: #fff; }

  .contact { position: absolute; font-size: 5.5px; line-height: 1.5; color: var(--muted); white-space: nowrap; }
  .site { position: absolute; color: #fff; font-size: 5.5px; z-index: 2; }

  .letterhead { left: 53px; top: 48px; width: 504px; height: 715px; }
  .letterhead .brand { left: 22px; top: 36px; }
  .letterhead .wordmark { font-size: 19px; }
  .letterhead .tagline { font-size: 6px; }
  .letterhead .contact { left: 194px; top: 26px; }
  .letterhead .wave { height: 75px; }
  .letterhead .site { right: 14px; bottom: 10px; }

  .card-front { left: 595px; top: 48px; width: 211px; height: 125px; border-radius: 6px; }
  .card-front .brand { left: 10px; top: 16px; }
  .card-front .wordmark { font-size: 12px; }
  .card-front .tagline { font-size: 4.5px; letter-spacing: 2px; margin-top: 2px; }
  .card-front .person { position: absolute; right: 12px; top: 14px; text-align: right; color: var(--wine); font-size: 5.5px; line-height: 1.35; }
  .card-front .contact { left: 12px; top: 58px; font-size: 4.8px; }
  .card-front .wave { height: 42px; }
  .card-front .site { right: 10px; bottom: 7px; font-size: 5px; }

  .card-back { left: 823px; top: 48px; width: 209px; height: 125px; border-radius: 8px; background: var(--wine); }
  .card-back .brand { left: 0; right: 0; top: 40px; }
  .card-back .wordmark { font-size: 17px; }
  .card-back .tagline { font-size: 5.5px; }

  .envelope-front { left: 595px; top: 197px; width: 547px; height: 295px; }
  .envelope-front .brand { left: 20px; top: 28px; }
  .envelope-front .wordmark { font-size: 18px; }
  .envelope-front .tagline { font-size: 6px; }
  .envelope-front .contact { left: 192px; top: 18px; }
  .envelope-front .wave { height: 84px; }
  .envelope-front .site { right: 14px; bottom: 10px; }

  .envelope-back { left: 595px; top: 516px; width: 547px; height: 283px; }
  .envelope-back .flap { position: absolute; left: 0; top: 0; width: 100%; height: 92px; }
  .envelope-back .brand { left: 0; right: 0; top: 24px; }
  .envelope-back .wordmark { font-size: 18px; }
  .envelope-back .tagline { font-size: 6px; }
</style>
</head>
<body>

<section class="sheet letterhead">
  <div class="brand">
    <div class="wordmark">Copperleaf Grill</div>
    <div class="tagline">New Orleans</div>
  </div>
  <div class="contact">
    318 Ferrand Street<br>New Orleans, LA 70119<br>Phone: (504) 555-0142<br>Cell: (504) 555-0187<br>Email: dwhitcomb@copperleaf-eats.com
  </div>
  <svg class="wave" viewBox="0 0 100 40" preserveAspectRatio="none">
    <path d="M0,30 C30,20 60,12 100,5 L100,40 L0,40Z" fill="var(--wine)"/>
    <path d="M2,24 C30,35 55,22 100,5 C55,18 30,30 2,24Z" fill="#111"/>
  </svg>
  <div class="site">www.copperleaf-eats.com</div>
</section>

<section class="sheet card-front">
  <div class="brand">
    <div class="wordmark">Copperleaf Grill</div>
    <div class="tagline">New Orleans</div>
  </div>
  <div class="person">Danielle Whitcomb<br>Proprietor</div>
  <div class="contact">
    318 Ferrand Street New Orleans, LA 70119<br>Phone: (504) 555-0142<br>Cell: (504) 555-0187<br>Email: dwhitcomb@copperleaf-eats.com
  </div>
  <svg class="wave" viewBox="0 0 100 40" preserveAspectRatio="none">
    <path d="M0,26 C30,16 60,8 100,2 L100,40 L0,40Z" fill="var(--wine)"/>
    <path d="M2,22 C30,32 55,18 100,2 C55,14 30,28 2,22Z" fill="#111"/>
  </svg>
  <div class="site">www.copperleaf-eats.com</div>
</section>

<section class="sheet card-back">
  <div class="brand light">
    <div class="wordmark">Copperleaf Grill</div>
    <div class="tagline">New Orleans</div>
  </div>
</section>

<section class="sheet envelope-front">
  <div class="brand">
    <div class="wordmark">Copperleaf Grill</div>
    <div class="tagline">New Orleans</div>
  </div>
  <div class="contact">
    318 Ferrand Street<br>New Orleans, LA 70119<br>Phone: (504) 555-0142<br>Cell: (504) 555-0187<br>Email: dwhitcomb@copperleaf-eats.com
  </div>
  <svg class="wave" viewBox="0 0 100 40" preserveAspectRatio="none">
    <path d="M0,30 C30,20 60,12 100,5 L100,40 L0,40Z" fill="var(--wine)"/>
    <path d="M2,24 C30,35 55,22 100,5 C55,18 30,30 2,24Z" fill="#111"/>
  </svg>
  <div class="site">www.copperleaf-eats.com</div>
</section>

<section class="sheet envelope-back">
  <svg class="flap" viewBox="0 0 100 40" preserveAspectRatio="none">
    <path d="M0,0 L100,0 L100,26 L50,40 L0,26Z" fill="var(--wine)"/>
  </svg>
  <div class="brand light">
    <div class="wordmark">Copperleaf Grill</div>
    <div class="tagline">New Orleans</div>
  </div>
</section>

</body>
</html>
```